New Flyer Design Project for a KBTW Business

I have started an KBTW business and want to create a Flyer and Brochure.
We already have a webpage and logo.
Below link is a reference point
https://www.plimvarto.com.au/design/71834620
webpage is www.belvorcare.com.au
Please match the colour from the webpage and the colour from KBTW webpage.
I also like the tri-folded brochure.
I want pictures associated with the disability sector.
Please use
contact number to be (02) 7341 9256
Email : Enquire@belvorcare.com.au
Thank you.
Disability sector
Disability

```html
<!DOCTYPE html>
<html lang="en">
<head>
<meta charset="utf-8">
<title>Belvor Care – Tri-fold Brochure</title>
<link rel="stylesheet" href="https://fonts.googleapis.com/css2?family=Montserrat:wght@400;500;600;700;800&display=swap">
<style>
  :root {
    --canvas: #8fb1ba;
    --paper: #f4f5f5;
    --grey-mid: #cdcdcd;
    --slate: #2f5663;
    --slate-panel: #3b5b67;
    --teal: #4fbfc0;
    --teal-deep: #1f8a8c;
    --navy: #10131d;
    --ink: #151515;
    --white: #ffffff;
  }
  * { box-sizing: border-box; margin: 0; padding: 0; }
  html, body { width: 1200px; height: 900px; overflow: hidden; }
  body {
    background: var(--canvas);
    font-family: "Montserrat", sans-serif;
    color: var(--ink);
  }
  .brochure {
    position: absolute;
    left: 60px; top: 68px;
    width: 1080px; height: 764px;
    background: var(--paper);
    overflow: hidden;
    box-shadow: 0 18px 40px rgba(20, 50, 60, .25);
  }
  .brochure-layer { position: absolute; left: 0; top: 0; }
  .fold {
    position: absolute; top: 0; bottom: 0; width: 1px;
    background: rgba(0,0,0,.08);
  }
  .fold--one { left: 360px; }
  .fold--two { left: 720px; }

  /* Panel one */
  .brand {
    position: absolute; left: 40px; top: 44px;
    display: flex; align-items: center; gap: 10px;
  }
  .brand-dot { width: 28px; height: 28px; border-radius: 50%; background: var(--teal-deep); }
  .brand-name { font-weight: 700; font-size: 20px; color: var(--teal-deep); }
  .cover-title {
    position: absolute; left: 44px; top: 130px;
    font-weight: 800; font-size: 46px; line-height: 1; color: var(--slate);
    letter-spacing: -.5px;
  }
  .cover-subtitle {
    display: block; margin-top: 8px;
    font-weight: 400; font-size: 30px; color: var(--teal);
  }
  .cover-tagline {
    position: absolute; left: 70px; top: 292px;
    font-size: 15px; font-weight: 500; line-height: 1.35; color: var(--ink);
  }

  /* Panel two */
  .why-heading {
    position: absolute; left: 400px; top: 40px;
    font-weight: 800; font-size: 76px; line-height: 1; color: var(--teal-deep);
  }
  .why-subheading {
    position: absolute; left: 402px; top: 122px;
    font-weight: 700; font-size: 22px; color: var(--ink);
  }
  .why-text {
    position: absolute; left: 402px; top: 176px; width: 280px;
    font-size: 14px; line-height: 1.6; text-align: justify; color: var(--ink);
  }
  .contact-card {
    position: absolute; left: 470px; top: 610px;
    width: 232px; height: 112px;
    background: var(--navy); border-radius: 16px;
    padding: 16px 18px;
    display: flex; flex-direction: column; justify-content: center; gap: 8px;
    color: var(--white); font-style: normal;
  }
  .contact-row { display: flex; align-items: center; gap: 10px; font-weight: 600; font-size: 12px; white-space: nowrap; }
  .contact-row--phone { font-size: 16px; font-weight: 700; }
  .contact-row svg { flex: none; }

  /* Panel three */
  .values-heading {
    position: absolute; left: 750px; top: 46px;
    font-weight: 700; font-size: 26px; color: var(--teal);
  }
  .values-kicker {
    position: absolute; left: 752px; top: 80px;
    font-weight: 700; font-size: 12px; color: var(--ink);
  }
  .value {
    position: absolute; left: 770px; width: 270px;
    text-align: center; color: var(--white);
  }
  .value-icon { display: block; margin: 0 auto 6px; }
  .value-title { font-weight: 700; font-size: 15px; color: var(--teal); margin-bottom: 4px; }
  .value-text { font-size: 12px; line-height: 1.45; }
  .value--people { top: 356px; }
  .value--enrich { top: 478px; }
  .value--fun { top: 604px; }
  .value--fun .value-title { color: var(--slate); }
</style>
</head>
<body>
<main class="brochure">
  <svg class="brochure-layer" width="1080" height="764" viewBox="0 0 1080 764" aria-hidden="true">
    <defs>
      <linearGradient id="greyPanel" x1="0" y1="0" x2="1" y2="1">
        <stop offset="0" stop-color="#e6e6e6"/>
        <stop offset="1" stop-color="#c9c9c9"/>
      </linearGradient>
    </defs>
    <rect x="360" y="0" width="360" height="764" fill="url(#greyPanel)"/>
    <path d="M720 300 C650 380 600 480 560 560 L520 764 L720 764 Z" fill="var(--navy)"/>
    <path d="M430 764 C500 660 600 590 720 560 L720 764 Z" fill="var(--teal)"/>
    <path d="M0 590 C70 570 150 610 210 660 L210 764 L0 764 Z" fill="var(--teal)"/>
    <path d="M140 500 C200 440 300 420 380 450" fill="none" stroke="var(--grey-mid)" stroke-width="22"/>
    <path d="M130 492 C190 420 300 400 390 432" fill="none" stroke="var(--slate)" stroke-width="5"/>
    <path d="M720 360 C820 300 940 160 1080 150 L1080 764 L720 764 Z" fill="var(--slate-panel)"/>
    <path d="M720 600 C850 590 980 560 1080 520 L1080 764 L720 764 Z" fill="var(--teal)"/>
  </svg>

  <svg class="brochure-layer" width="1080" height="764" viewBox="0 0 1080 764" role="img" aria-label="Photo of two smiling young adults holding out their hands, one in a yellow shirt and one in a red jumper">
    <defs>
      <linearGradient id="peopleTones" x1="0" y1="0" x2="0" y2="1">
        <stop offset="0" stop-color="#e9ddc9"/>
        <stop offset="1" stop-color="#cf8f6e"/>
      </linearGradient>
    </defs>
    <rect x="180" y="450" width="340" height="314" fill="url(#peopleTones)"/>
  </svg>

  <svg class="brochure-layer" width="1080" height="764" viewBox="0 0 1080 764" role="img" aria-label="Black and white photo of a young woman reading with a support worker">
    <defs>
      <linearGradient id="greyTones" x1="0" y1="0" x2="1" y2="1">
        <stop offset="0" stop-color="#a8a8a8"/>
        <stop offset="1" stop-color="#e4e4e4"/>
      </linearGradient>
    </defs>
    <path d="M770 330 C800 200 900 90 1080 70 L1080 150 C940 160 820 300 720 360 Z" fill="url(#greyTones)"/>
  </svg>

  <div class="fold fold--one"></div>
  <div class="fold fold--two"></div>

  <section class="panel panel--cover">
    <div class="brand">
      <span class="brand-dot"></span>
      <span class="brand-name">Belvor Care</span>
    </div>
    <h1 class="cover-title">Disability<br>Support<span class="cover-subtitle">Provider</span></h1>
    <p class="cover-tagline">At Belvor Care,<br>we're life enhancers!</p>
  </section>

  <section class="panel panel--about">
    <h2 class="why-heading">Why</h2>
    <p class="why-subheading">Choose Belvor Care?</p>
    <p class="why-text">Belvor Care was born out of a desire to make a real and lasting difference in the lives of our participants and the wider community. We approach each individual with empathy, respect, and a deep commitment to understanding their unique story, needs, and aspirations.</p>
    <address class="contact-card">
      <span class="contact-row contact-row--phone">
        <svg width="16" height="16" viewBox="0 0 24 24" fill="none" stroke="#fff" stroke-width="2"><path d="M5 3h4l2 5-3 2a12 12 0 0 0 6 6l2-3 5 2v4a2 2 0 0 1-2 2A18 18 0 0 1 3 5a2 2 0 0 1 2-2z"/></svg>
        (02) 7341 9256
      </span>
      <span class="contact-row">
        <svg width="16" height="16" viewBox="0 0 24 24" fill="none" stroke="#fff" stroke-width="2"><rect x="3" y="5" width="18" height="14" rx="2"/><path d="M3 7l9 6 9-6"/></svg>
        Enquire@belvorcare.com.au
      </span>
      <span class="contact-row">
        <svg width="16" height="16" viewBox="0 0 24 24" fill="none" stroke="#fff" stroke-width="2"><circle cx="12" cy="12" r="9"/><path d="M3 12h18M12 3c3 3 3 15 0 18M12 3c-3 3-3 15 0 18"/></svg>
        belvorcare.com.au
      </span>
    </address>
  </section>

  <section class="panel panel--values">
    <h2 class="values-heading">Empowering</h2>
    <p class="values-kicker">Lives in NSW</p>

    <div class="value value--people">
      <svg class="value-icon" width="26" height="24" viewBox="0 0 24 22"><path d="M12 20S2 13.5 2 7.5A5 5 0 0 1 12 5a5 5 0 0 1 10 2.5C22 13.5 12 20 12 20z" fill="#fff" stroke="var(--teal)" stroke-width="2"/></svg>
      <p class="value-title">People &amp; Family Oriented</p>
      <p class="value-text">We see each participant as part of our extended family, ensuring a warm, personal touch in everything we do.</p>
    </div>

    <div class="value value--enrich">
      <svg class="value-icon" width="26" height="26" viewBox="0 0 24 24" fill="none" stroke="var(--teal)" stroke-width="2"><circle cx="12" cy="12" r="9"/><circle cx="9" cy="10" r="1" fill="var(--teal)"/><circle cx="15" cy="10" r="1" fill="var(--teal)"/><path d="M8 14c2 2.5 6 2.5 8 0"/></svg>
      <p class="value-title">Enriching Lives</p>
      <p class="value-text">Every day, we're fuelled by our mission to make a tangible difference in the community.</p>
    </div>

    <div class="value value--fun">
      <svg class="value-icon" width="22" height="28" viewBox="0 0 22 28" fill="none" stroke="var(--slate)" stroke-width="2.4"><circle cx="11" cy="9" r="7"/><path d="M11 16v11"/></svg>
      <p class="value-title">Fun &amp; Fulfilment</p>
      <p class="value-text">We believe in adding a dash of fun to our services because a joyful journey is as important as the destination.</p>
    </div>
  </section>
</main>
</body>
</html>
```